Bar Wanderlight VIP Card design

Looking for a design for a VIP card forguests wishing to purchase to avoid cover charges, skipping the line and othe advantages.

We used our logo on last years card.I've also attached a few of our previous cards. Looking for something fresh.

We are not apposed to a vertical card either way would be fine We will have to incorporate the fizz mild logo on the card as well.

Industry/Entity Type

Bar Restaurant www.bar-w.example

Font styles to use
Decorative

```html
<!DOCTYPE html>
<html lang="en">
<head>
<meta charset="utf-8">
<title>Bar Wanderlight VIP Card</title>
<link rel="stylesheet" href="https://fonts.googleapis.com/css2?family=Poppins:wght@700&family=Allura&display=swap">
<style>
  :root {
    --page: #ffffff;
    --night-left: #221a42;
    --night-right: #40196f;
    --panel-top: #62158f;
    --panel-mid: #4a078a;
    --panel-low: #1e1040;
    --frame-orange: #f7a23b;
    --script-orange: #f7a23b;
    --script-shadow: #a8a8a8;
    --white: #ffffff;
    --ray: rgba(255, 255, 255, 0.16);
    --bloom-pink: #ef7a6a;
    --bloom-leaf: #3f5f7d;
  }
  * { margin: 0; padding: 0; box-sizing: border-box; }
  html, body {
    width: 1200px;
    height: 1200px;
    overflow: hidden;
    background: var(--page);
  }
  .vip-card {
    position: absolute;
    left: 239px;
    top: 366px;
    width: 722px;
    height: 467px;
    overflow: hidden;
    background: linear-gradient(100deg, var(--night-left), var(--night-right));
  }
  .vip-card svg { position: absolute; inset: 0; display: block; }
  .floral-corner {
    position: absolute;
    background: radial-gradient(circle at 60% 45%, var(--bloom-pink) 0 28%, rgba(239,122,106,0.55) 40%, rgba(63,95,125,0.7) 62%, rgba(63,95,125,0) 78%);
  }
  .floral-corner--top-right {
    left: 506px; top: -20px; width: 240px; height: 290px;
    border-radius: 50% 0 40% 60%;
  }
  .floral-corner--bottom-left {
    left: -24px; top: 196px; width: 230px; height: 290px;
    border-radius: 40% 60% 0 50%;
  }
  .venue-mark {
    position: absolute;
    left: 22px;
    top: 70px;
    display: flex;
    align-items: center;
    gap: 6px;
    font-family: "Poppins", sans-serif;
    font-weight: 700;
    font-size: 13px;
    color: var(--frame-orange);
    letter-spacing: 0.02em;
  }
  .venue-mark__dot {
    width: 16px; height: 16px;
    border-radius: 50%;
    background: var(--frame-orange);
  }
  .partner-mark {
    position: absolute;
    left: 576px;
    top: 354px;
    font-family: "Poppins", sans-serif;
    font-weight: 700;
    font-size: 15px;
    line-height: 1;
    color: var(--white);
  }
</style>
</head>
<body>
  <main class="vip-card">
    <svg width="722" height="467" viewBox="0 0 722 467" aria-hidden="true">
      <defs>
        <linearGradient id="panel-fill" x1="0" y1="0" x2="0" y2="1">
          <stop offset="0" stop-color="var(--panel-top)"/>
          <stop offset="0.45" stop-color="var(--panel-mid)"/>
          <stop offset="1" stop-color="var(--panel-low)"/>
        </linearGradient>
        <filter id="glow" x="-20%" y="-20%" width="140%" height="140%">
          <feGaussianBlur stdDeviation="6" result="b"/>
          <feMerge><feMergeNode in="b"/><feMergeNode in="SourceGraphic"/></feMerge>
        </filter>
      </defs>
      <rect class="feature-panel" x="55" y="62" width="612" height="342" fill="url(#panel-fill)"/>
      <g class="light-rays" stroke="var(--ray)" stroke-width="3">
        <line x1="0" y1="6" x2="400" y2="467"/>
        <line x1="0" y1="37" x2="587" y2="467"/>
        <line x1="22" y1="0" x2="722" y2="428"/>
        <line x1="53" y1="0" x2="722" y2="286"/>
      </g>
    </svg>

    <div class="floral-corner floral-corner--top-right" role="img" aria-label="Watercolour tropical flowers and leaves"></div>
    <div class="floral-corner floral-corner--bottom-left" role="img" aria-label="Watercolour tropical flowers and leaves"></div>

    <svg width="722" height="467" viewBox="0 0 722 467">
      <rect class="feature-frame" x="55" y="62" width="612" height="342" fill="none" stroke="var(--frame-orange)" stroke-width="4"/>
      <text class="vip-title" x="168" y="332" textLength="381" lengthAdjust="spacingAndGlyphs"
            font-family="Poppins, sans-serif" font-weight="700" font-size="306" fill="var(--white)" filter="url(#glow)">VIP</text>
      <text class="venue-script-shadow" x="146" y="309" textLength="447" lengthAdjust="spacingAndGlyphs"
            font-family="Allura, cursive" font-size="82" fill="var(--script-shadow)" aria-hidden="true">Bar Wanderlight</text>
      <text class="venue-script" x="140" y="304" textLength="447" lengthAdjust="spacingAndGlyphs"
            font-family="Allura, cursive" font-size="82" fill="var(--script-orange)">Bar Wanderlight</text>
      <g class="sparkles" fill="var(--white)">
        <path d="M551 120 L554 129 L563 132 L554 135 L551 144 L548 135 L539 132 L548 129 Z"/>
        <path d="M172 185 L174 191 L180 193 L174 195 L172 201 L170 195 L164 193 L170 191 Z"/>
        <path d="M363 341 L364 344 L367 345 L364 346 L363 349 L362 346 L359 345 L362 344 Z"/>
      </g>
    </svg>

    <div class="venue-mark"><span class="venue-mark__dot"></span>Bar Wanderlight</div>
    <div class="partner-mark">FIZZ MILD</div>
  </main>
</body>
</html>
```